FinTech Website + Mobile Design.

We require an new fresh Professional looking upgrade for our company website.

We are Australia's first professional crowd funding platform. Currently listed on the QMB(Meridian Trading Board) and soon to be listed on the KPR(Harbourline Equity Market)

We are looking for a clean simple but professional look with clear focus the two main objectives "Investing" and "Borrowing"

Veltrano is a professional crowdfunding platform focused at servicing SME’s and non-sophisticated Investors.
Our platform lets borrowers access funds of $100,000 to $5 Million form our user base of over 50,000 members. Borrowers choose the rate they are prepared offer Investors and Investors select the opportunities they would like to invest in with average returns of 12%pa*.

Our platform gives Investors and borrows a real alternative to conventional banking. Funding can be done in as little as 45days*.

We need the design to be responsive.

The are some Charts and Statistics that will need graphics producing.

We will require Photoshop files, fonts and assets only. Not HTML or CSS.

Reference sites
https://plovenest.com
https://www.brambleworth.com
https://www.zenquarrow.com
https://au.trelvingsharedesk.com/
Updates

This project has been extended by 5 Days. I look forward to see your designs. Cheers Wendell

Dear Designers, Please don't forget to include a Mobile version of your designs. Thanks Wendell

Hi All Designers, I will be closing this project in two days. Don't miss out. Get your designs in as soon as you can. Cheers Wendell

Target Market(s)

Investors, Property developers, Small business' Medium business.

Industry/Entity Type

Finance

Number of Pages Required

1 page

Font styles to use
Sans Serif

Requirements
Must have
• Clean Professional design
• Bright and fresh look
• Mobile design/responsive
Nice to have
• Animations

```html
<!DOCTYPE html>
<html lang="en">
<head>
<meta charset="utf-8">
<title>Veltrano — Crowd Funding Platform</title>
<link href="https://fonts.googleapis.com/css2?family=Raleway:wght@300;400;500;600;700&family=Open+Sans:wght@400;600;700&display=swap" rel="stylesheet">
<style>
:root{
  --yellow:#f5cf0c;
  --yellow-dark:#e0b800;
  --red:#c8262c;
  --orange:#f7941d;
  --green:#35d97a;
  --blue:#3a9ef0;
  --ink:#2d2d2d;
  --grey:#6b6b6b;
  --light:#f2f2f2;
  --footer:#2a2a2a;
  --footer-deep:#1d1d1d;
  --white:#ffffff;
}
*{box-sizing:border-box;margin:0;padding:0}
html,body{width:1200px;height:4604px;overflow:hidden}
body{font-family:"Open Sans",sans-serif;color:var(--ink);background:var(--white);position:relative}
section,header,footer{position:relative;width:1200px;overflow:hidden}
.abs{position:absolute}
h2.section-title{font-family:"Raleway",sans-serif;font-weight:400;font-size:42px;text-align:center;color:var(--ink)}

/* hero */
.hero{height:712px;background:linear-gradient(180deg,#4a6a8c 0%,#6f8fa8 40%,#8ea5b3 70%,#5c6f7c 100%)}
.hero-photo{position:absolute;inset:0;background:linear-gradient(160deg,rgba(40,70,110,.6),rgba(150,170,180,.2) 60%,rgba(40,50,60,.5))}
.brand{left:82px;top:34px;display:flex;align-items:center;gap:10px;font-family:"Raleway",sans-serif;font-weight:700;font-size:32px;color:var(--white)}
.brand-dot{width:30px;height:30px;border-radius:50%;background:var(--yellow)}
.nav{right:64px;top:44px;display:flex;align-items:center;gap:26px;font-family:"Raleway",sans-serif;font-size:15px;color:var(--white)}
.nav .pill{padding:5px 14px;border-radius:14px;font-weight:600;font-size:13px}
.pill.login{background:var(--yellow);color:var(--ink)}
.pill.signup{background:var(--red);color:var(--white)}
.hero-title{top:308px;width:100%;text-align:center;font-family:"Raleway",sans-serif;font-weight:400;font-size:38px;color:var(--white)}
.hero-sub{top:372px;width:100%;display:flex;justify-content:center;align-items:center;gap:18px;font-family:"Raleway",sans-serif;font-weight:600;font-size:23px;color:var(--white)}
.hero-sub .sep{width:22px;height:22px;border-radius:50%;border:4px solid var(--yellow)}
.cta-signup{top:442px;left:440px;width:320px;height:66px;border:3px solid var(--yellow);border-radius:33px;background:rgba(20,20,20,.45);color:var(--white);font-family:"Raleway",sans-serif;font-weight:600;font-size:25px;display:flex;align-items:center;justify-content:center}

.news{height:80px;background:var(--yellow)}
.news-label{left:0;top:0;width:260px;height:80px;background:var(--yellow-dark);display:flex;align-items:center;justify-content:flex-end;padding-right:48px;font-family:"Raleway",sans-serif;font-weight:700;font-size:20px;color:var(--ink)}
.news-text{left:288px;top:16px;width:590px}
.news-text strong{display:block;font-family:"Raleway",sans-serif;font-size:18px;color:var(--ink);white-space:nowrap}
.news-text span{display:block;font-size:12px;color:#5a4a00;margin-top:4px;white-space:nowrap}
.news-date{left:890px;top:24px;font-size:13px;color:#5a4a00}
.news-arrows{left:1020px;top:26px;display:flex;gap:14px}

/* projects */
.projects{height:550px;background:var(--white)}
.projects h2{padding-top:48px}
.slide-arrow{top:230px}
.project-card{top:138px;width:246px;height:334px;background:var(--white);box-shadow:0 2px 8px rgba(0,0,0,.18)}
.project-photo{height:150px}
.project-body{padding:10px 12px 0}
.project-desc{font-size:12px;line-height:16px;height:48px;overflow:hidden;color:var(--ink)}
.project-loc{display:flex;align-items:center;gap:6px;font-size:12px;font-weight:600;margin-top:4px}
.funded{margin-top:16px;text-align:center;font-size:12px;font-weight:700;color:var(--red)}
.funded-bar{height:5px;background:var(--red);margin-top:3px}
.project-stats{position:absolute;left:0;bottom:0;width:100%;height:54px;background:var(--ink);display:flex;color:var(--white)}
.project-stats div{flex:1;text-align:center;padding-top:11px;font-size:12px;font-weight:700;line-height:16px;white-space:nowrap}
.project-stats div:last-child{flex:1.4}
.project-stats small{display:block;font-size:9px;font-weight:400;color:#bbb}

/* chart */
.growth{height:638px;background:linear-gradient(135deg,#c0314e 0%,#8e2b52 45%,#4b1f4d 100%)}
.growth h2{position:absolute;top:64px;left:150px;width:900px;text-align:center;font-family:"Raleway",sans-serif;font-weight:400;font-size:38px;line-height:50px;color:var(--white)}
.growth-badge{border-radius:50%;display:flex;flex-direction:column;align-items:center;justify-content:center;font-family:"Raleway",sans-serif;font-size:13px;color:var(--ink)}
.growth-badge b{font-size:40px;line-height:44px;font-weight:600}
.badge-estate{left:1020px;top:160px;width:124px;height:124px;background:var(--yellow)}
.badge-market{left:1020px;top:350px;width:124px;height:124px;background:var(--white);box-shadow:0 0 0 6px rgba(255,255,255,.3)}
.growth-caption{top:560px;width:100%;text-align:center;font-size:13px;color:var(--white)}

/* stats */
.stats{height:544px}
.stats h2{padding-top:68px}
.stats-intro{width:900px;margin:24px auto 0;text-align:center;font-size:15px;line-height:28px;color:var(--grey)}
.stats-intro b{color:var(--ink)}
.stat-ring{top:218px;width:228px;height:228px;border-radius:50%;border:9px solid;display:flex;flex-direction:column;align-items:center;justify-content:center;text-align:center;box-shadow:0 3px 10px rgba(0,0,0,.12)}
.stat-ring b{font-family:"Raleway",sans-serif;font-weight:500;font-size:40px;color:var(--ink);white-space:nowrap}
.stat-ring p{font-size:13px;line-height:17px;color:var(--grey);width:150px;margin-top:6px}

/* events */
.events{height:576px;background:var(--light)}
.events h2{padding-top:52px}
.event-card{top:140px;width:324px;height:362px;background:var(--white);box-shadow:0 2px 8px rgba(0,0,0,.15)}
.event-photo{height:160px}
.event-date{position:absolute;left:30px;top:110px;width:76px;height:76px;border-radius:50%;background:var(--red);color:var(--white);text-align:center;font-family:"Raleway",sans-serif;font-weight:600;font-size:28px;line-height:30px;padding-top:12px}
.event-date small{display:block;font-size:11px;line-height:12px}
.event-body{padding:36px 18px 0}
.event-body h3{font-family:"Raleway",sans-serif;font-weight:500;font-size:16px}
.event-by{font-size:11px;color:#999;font-style:normal;margin-top:2px}
.event-time{display:flex;align-items:center;gap:6px;font-size:12px;font-weight:700;margin-top:8px}
.event-desc{font-size:12px;line-height:17px;color:var(--grey);margin-top:10px}
.event-more{position:absolute;right:18px;bottom:14px;width:22px;height:22px;border-radius:50%;background:var(--yellow)}

/* collective banner */
.collective{height:575px;background:linear-gradient(180deg,#1f2a36 0%,#3d4a55 55%,#2a2e33 100%)}
.collective-name{top:262px;width:100%;text-align:center;font-family:"Raleway",sans-serif;font-weight:300;font-size:70px;letter-spacing:2px;color:var(--white);white-space:nowrap}
.collective-tag{top:350px;width:100%;text-align:center;font-family:"Raleway",sans-serif;font-size:20px;color:#d8dde3}
.explore{left:490px;top:404px;width:220px;height:60px;border-radius:30px;background:var(--red);color:var(--white);font-family:"Raleway",sans-serif;font-weight:600;font-size:19px;display:flex;align-items:center;justify-content:center}

/* featured */
.featured{height:315px}
.featured h2{padding-top:54px}
.press-logo{top:148px;width:192px;height:86px;border:1px solid #ddd;display:flex;align-items:center;justify-content:center;font-family:"Raleway",sans-serif;font-weight:700;font-size:20px;color:var(--ink);white-space:nowrap}

/* footer */
.site-footer{height:535px;background:var(--footer);color:#cfcfcf}
.site-footer h4{font-family:"Raleway",sans-serif;font-weight:500;font-size:19px;color:var(--white);margin-bottom:12px}
.foot-col{font-size:13px;line-height:20px}
.foot-col li{list-style:none}
.foot-col li::before{content:"› ";color:var(--yellow)}
.contact-line{display:flex;gap:8px;align-items:flex-start;margin-bottom:10px}
.contact-line svg{flex:none;margin-top:3px}
.map{width:240px;height:136px;background:linear-gradient(135deg,#e6e3dc,#cfd8cf)}
.badge-block{background:#e8e8e8}
.social{display:flex;gap:8px}
.social span{width:30px;height:30px;border-radius:50%;border:2px solid #888}
.copyright{height:79px;background:var(--footer-deep);color:#bbb;font-size:12px}
.copyright .note{left:82px;top:30px}
.copyright .foot-brand{right:82px;top:24px;display:flex;gap:8px;align-items:center;font-family:"Raleway",sans-serif;font-weight:700;font-size:22px;color:var(--white)}
</style>
</head>
<body>

<header class="hero">
  <div class="hero-photo" role="img" aria-label="Photo of a coastal city skyline with high-rise towers along the beach"></div>
  <div class="brand abs"><span class="brand-dot"></span>Veltrano</div>
  <nav class="nav abs">
    <span>Crowdfunding</span><span>Business Loan</span><span>About Us</span><span>Events</span><span>Valuation Tool</span>
    <span class="pill login">Login</span><span class="pill signup">Sign Up</span>
  </nav>
  <h1 class="hero-title abs">We Are Australia First Professional Crowd Funding Platform.</h1>
  <div class="hero-sub abs"><span>12%pa* Average Returns</span><span class="sep"></span><span>50,000 User Base</span><span class="sep"></span><span>Fundraising in Just 45 Days</span></div>
  <div class="cta-signup abs">SIGN UP FOR FREE</div>
</header>

<section class="news">
  <div class="news-label abs">NEWS</div>
  <div class="news-text abs"><strong>Lorem ipsum dolor sit amet, consectetuer adipiscing elit, sed diam</strong><span>New property listings open this week with returns targeted above twelve percent a year.</span></div>
  <div class="news-date abs">29 June, 2016</div>
  <div class="news-arrows abs">
    <svg width="14" height="26" viewBox="0 0 14 26"><path d="M12 2 2 13l10 11" fill="none" stroke="#2d2d2d" stroke-width="3"/></svg>
    <svg width="14" height="26" viewBox="0 0 14 26"><path d="M2 2l10 11L2 24" fill="none" stroke="#2d2d2d" stroke-width="3"/></svg>
  </div>
</section>

<section class="projects">
  <h2 class="section-title">Our Successful Projects</h2>
  <svg class="slide-arrow abs" style="left:34px" width="16" height="36" viewBox="0 0 16 36"><path d="M14 2 2 18l12 16" fill="none" stroke="#888" stroke-width="3"/></svg>
  <svg class="slide-arrow abs" style="left:1150px" width="16" height="36" viewBox="0 0 16 36"><path d="M2 2l12 16L2 34" fill="none" stroke="#888" stroke-width="3"/></svg>

  <article class="project-card abs" style="left:82px">
    <div class="project-photo" role="img" aria-label="Photo of a restaurant reception counter" style="background:linear-gradient(135deg,#8a5a3c,#c79a6e)"></div>
    <div class="project-body">
      <p class="project-desc">Help Harlow Meadow Foods crowdfund an international F&amp;B franchise outlet today!</p>
      <p class="project-loc"><svg width="10" height="13" viewBox="0 0 10 13"><path d="M5 0a5 5 0 0 0-5 5c0 4 5 8 5 8s5-4 5-8a5 5 0 0 0-5-5z" fill="#2d2d2d"/><circle cx="5" cy="5" r="2" fill="#fff"/></svg>Fujian, China</p>
      <p class="funded">Successfully Funded</p><div class="funded-bar"></div>
    </div>
    <div class="project-stats"><div>14%<small>Total Yield</small></div><div>6<small>Tenure(mth)</small></div><div>End Of Tenure<small>Payout Freq.</small></div></div>
  </article>

  <article class="project-card abs" style="left:346px">
    <div class="project-photo" role="img" aria-label="Photo of a bright clinic lobby" style="background:linear-gradient(135deg,#cfd6dc,#8d99a4)"></div>
    <div class="project-body">
      <p class="project-desc">Receive 10% P.A returns by crowdfunding Verdant Clinic – a health and beauty products...</p>
      <p class="project-loc"><svg width="10" height="13" viewBox="0 0 10 13"><path d="M5 0a5 5 0 0 0-5 5c0 4 5 8 5 8s5-4 5-8a5 5 0 0 0-5-5z" fill="#2d2d2d"/><circle cx="5" cy="5" r="2" fill="#fff"/></svg>Singapore, Singapore</p>
      <p class="funded">Successfully Funded</p><div class="funded-bar"></div>
    </div>
    <div class="project-stats"><div>10%<small>Total Yield</small></div><div>6<small>Tenure(mth)</small></div><div>End Of Tenure<small>Payout Freq.</small></div></div>
  </article>

  <article class="project-card abs" style="left:610px">
    <div class="project-photo" role="img" aria-label="Photo of a furnished apartment interior" style="background:linear-gradient(135deg,#6e4a34,#b8875e)"></div>
    <div class="project-body">
      <p class="project-desc">Lomara Estate – Phase 3</p>
      <p class="project-loc"><svg width="10" height="13" viewBox="0 0 10 13"><path d="M5 0a5 5 0 0 0-5 5c0 4 5 8 5 8s5-4 5-8a5 5 0 0 0-5-5z" fill="#2d2d2d"/><circle cx="5" cy="5" r="2" fill="#fff"/></svg>Shengai, China</p>
      <p class="funded">Successfully Funded</p><div class="funded-bar"></div>
    </div>
    <div class="project-stats"><div>14%<small>Total Yield</small></div><div>6<small>Tenure(mth)</small></div><div>End Of Tenure<small>Payout Freq.</small></div></div>
  </article>

  <article class="project-card abs" style="left:874px">
    <div class="project-photo" role="img" aria-label="Photo of a restaurant dining room" style="background:linear-gradient(135deg,#5a2a22,#a0584a)"></div>
    <div class="project-body">
      <p class="project-desc">Harlow Meadow Foods is Crowdfunding another International F&amp;B Chain Outlet!</p>
      <p class="project-loc"><svg width="10" height="13" viewBox="0 0 10 13"><path d="M5 0a5 5 0 0 0-5 5c0 4 5 8 5 8s5-4 5-8a5 5 0 0 0-5-5z" fill="#2d2d2d"/><circle cx="5" cy="5" r="2" fill="#fff"/></svg>Fujian, China</p>
      <p class="funded">Successfully Funded</p><div class="funded-bar"></div>
    </div>
    <div class="project-stats"><div>14%<small>Total Yield</small></div><div>6<small>Tenure(mth)</small></div><div>End Of Tenure<small>Payout Freq.</small></div></div>
  </article>
</section>

<section class="growth">
  <h2>Did You Know? Investors Who Diversify Into Real<br>Estate Outperform Those Who Don't.</h2>
  <svg class="abs" style="left:120px;top:190px" width="900" height="360" viewBox="0 0 900 360" font-family="Open Sans, sans-serif" font-size="12" fill="#fff">
    <g stroke="rgba(255,255,255,.25)" stroke-dasharray="3 4">
      <line x1="30" y1="60" x2="860" y2="60"/><line x1="30" y1="130" x2="860" y2="130"/><line x1="30" y1="200" x2="860" y2="200"/><line x1="30" y1="270" x2="860" y2="270"/>
    </g>
    <path d="M30 320 L80 312 L120 300 L150 306 L190 290 L230 282 L270 270 L300 250 L330 262 L360 238 L400 222 L440 200 L470 215 L500 208 L520 140 L545 160 L570 128 L600 112 L630 124 L660 100 L690 108 L720 92 L750 70 L780 84 L810 62 L830 70 L830 320 Z" fill="rgba(245,207,12,.3)"/>
    <path d="M30 320 L80 312 L120 300 L150 306 L190 290 L230 282 L270 270 L300 250 L330 262 L360 238 L400 222 L440 200 L470 215 L500 208 L520 140 L545 160 L570 128 L600 112 L630 124 L660 100 L690 108 L720 92 L750 70 L780 84 L810 62 L830 70" fill="none" stroke="#f5cf0c" stroke-width="3"/>
    <path d="M30 320 L90 300 L140 306 L190 316 L240 322 L290 312 L340 300 L390 292 L430 310 L470 318 L510 300 L560 292 L610 284 L660 274 L710 262 L760 244 L800 226 L830 206" fill="none" stroke="#e0243a" stroke-width="3"/>
    <line x1="30" y1="320" x2="860" y2="320" stroke="#fff" stroke-width="2"/>
    <g font-weight="700" text-anchor="middle">
      <text x="30" y="342">2000</text><text x="130" y="342">2002</text><text x="230" y="342">2004</text><text x="330" y="342">2006</text><text x="430" y="342">2008</text><text x="530" y="342">2010</text><text x="630" y="342">2012</text><text x="730" y="342">2014</text><text x="830" y="342">2016</text>
    </g>
  </svg>
  <div class="growth-badge badge-estate abs">Real Estate<b>482%</b>Growth</div>
  <div class="growth-badge badge-market abs">BMX 500<b>80%</b>Growth</div>
  <p class="growth-caption abs">Meridian REIT Composite vs. BMX 500, Growth in Percentage, Jan 1 2000–Dec 31 2015 (dividends reinvested)</p>
</section>

<section class="stats">
  <h2 class="section-title">Here Are Some Of The Stats &amp; Figures</h2>
  <p class="stats-intro">We are professional crowd funding platform focused at servicing Small &amp; medium enterprises / businesses and non-sophisticated Investors. <b>We are Australia first professional crowd funding platform.</b></p>
  <div class="stat-ring abs" style="left:116px;border-color:var(--yellow)"><b>12.0%<small style="font-size:14px">pa</small></b><p>Opportunities To Invest With Average Returns</p></div>
  <div class="stat-ring abs" style="left:362px;border-color:var(--orange)"><b>$5 Million</b><p>Lets Borrowers Access Funds In Millions</p></div>
  <div class="stat-ring abs" style="left:614px;border-color:var(--green)"><b>50,000</b><p>Members Using The Platform For Fundraising</p></div>
  <div class="stat-ring abs" style="left:868px;border-color:var(--blue)"><b>45 Days</b><p>Funding Can Be Done In A Very Small Time Span</p></div>
</section>

<section class="events">
  <h2 class="section-title">Upcoming Events</h2>
  <article class="event-card abs" style="left:83px">
    <div class="event-photo" role="img" aria-label="Photo of a city skyline at dusk over water" style="background:linear-gradient(180deg,#2d4c7a,#7d93b8)"></div>
    <div class="event-date">17<small>JUNE</small></div>
    <div class="event-body"><h3>Collaboration for your New Future</h3><p class="event-by">By Veltrano Pte Ltd</p>
      <p class="event-time"><svg width="12" height="12" viewBox="0 0 12 12"><circle cx="6" cy="6" r="5" fill="none" stroke="#f5cf0c" stroke-width="2"/><path d="M6 3v3h2" stroke="#f5cf0c" stroke-width="1.5" fill="none"/></svg>14:00 – 17:00</p>
      <p class="event-desc">Lorem ipsum dolor sit amet, consectet uer adipiscing elit, sed diam</p></div>
    <span class="event-more"></span>
  </article>
  <article class="event-card abs" style="left:438px">
    <div class="event-photo" role="img" aria-label="Photo of a lit tower at night" style="background:linear-gradient(180deg,#1c2850,#5b4a8a)"></div>
    <div class="event-date">17<small>JUNE</small></div>
    <div class="event-body"><h3>Collaboration for your New Future</h3><p class="event-by">By Veltrano Pte Ltd</p>
      <p class="event-time"><svg width="12" height="12" viewBox="0 0 12 12"><circle cx="6" cy="6" r="5" fill="none" stroke="#f5cf0c" stroke-width="2"/><path d="M6 3v3h2" stroke="#f5cf0c" stroke-width="1.5" fill="none"/></svg>14:00 – 17:00</p>
      <p class="event-desc">Lorem ipsum dolor sit amet, consectet uer adipiscing elit, sed diam</p></div>
    <span class="event-more"></span>
  </article>
  <article class="event-card abs" style="left:793px">
    <div class="event-photo" role="img" aria-label="Photo of downtown office towers" style="background:linear-gradient(180deg,#8fb0cf,#c9b394)"></div>
    <div class="event-date">17<small>JUNE</small></div>
    <div class="event-body"><h3>Collaboration for your New Future</h3><p class="event-by">By Veltrano Pte Ltd</p>
      <p class="event-time"><svg width="12" height="12" viewBox="0 0 12 12"><circle cx="6" cy="6" r="5" fill="none" stroke="#f5cf0c" stroke-width="2"/><path d="M6 3v3h2" stroke="#f5cf0c" stroke-width="1.5" fill="none"/></svg>14:00 – 17:00</p>
      <p class="event-desc">Lorem ipsum dolor sit amet, consectet uer adipiscing elit, sed diam</p></div>
    <span class="event-more"></span>
  </article>
</section>

<section class="collective" role="img" aria-label="Aerial photo of a city skyline at dusk">
  <div class="collective-name abs">VELTRANO COLLECTIVE</div>
  <div class="collective-tag abs">Crowdfunding Everything. Everything Crowdfunding</div>
  <div class="explore abs">EXPLORE MORE</div>
</section>

<section class="featured">
  <h2 class="section-title">Featured On</h2>
  <svg class="abs" style="left:34px;top:172px" width="16" height="36" viewBox="0 0 16 36"><path d="M14 2 2 18l12 16" fill="none" stroke="#888" stroke-width="3"/></svg>
  <svg class="abs" style="left:1150px;top:172px" width="16" height="36" viewBox="0 0 16 36"><path d="M2 2l12 16L2 34" fill="none" stroke="#888" stroke-width="3"/></svg>
  <div class="press-logo abs" style="left:83px">Nexa News</div>
  <div class="press-logo abs" style="left:291px">Corvane</div>
  <div class="press-logo abs" style="left:499px">Dunmore Times</div>
  <div class="press-logo abs" style="left:707px">Techvally</div>
  <div class="press-logo abs" style="left:915px">The Ledger Daily</div>
</section>

<footer class="site-footer">
  <div class="foot-col abs" style="left:83px;top:40px">
    <h4>Quick Links</h4>
    <ul><li>Crowdfunding</li><li>Business Loan</li><li>About Us</li><li>Events</li><li>Valuation Tool</li><li>Corporate</li><li>Projects</li><li>News</li></ul>
    <h4 style="margin-top:48px">Terms</h4>
    <ul><li>Terms of Use</li><li>Code of Conduct</li><li>Privacy Policy</li><li>FAQ</li></ul>
  </div>
  <div class="foot-col abs" style="left:313px;top:40px;width:220px">
    <h4>For Developers</h4>
    <ul><li>Get in touch with us to find out how you can list your projects.</li></ul>
    <h4 style="margin-top:28px">For Investors</h4>
    <ul><li>Find out more about Veltrano here.</li></ul>
    <h4 style="margin-top:48px">Media Relation</h4>
    <ul><li>Get in touch with us here.</li></ul>
    <h4 style="margin-top:28px">Media Partner</h4>
    <ul><li>FundPulse Weekly</li><li>RaiseMapper</li></ul>
  </div>
  <div class="foot-col abs" style="left:580px;top:40px;width:260px">
    <h4>Contact Details</h4>
    <p class="contact-line"><svg width="12" height="15" viewBox="0 0 10 13"><path d="M5 0a5 5 0 0 0-5 5c0 4 5 8 5 8s5-4 5-8a5 5 0 0 0-5-5z" fill="#f5cf0c"/></svg><span>Veltrano Ltd. (ACN 000 412 905) Suite 4, Level 2, 88 Calder Street East Perth WA 6004</span></p>
    <p class="contact-line"><svg width="13" height="13" viewBox="0 0 13 13"><path d="M3 0 5 3 3.5 5a8 8 0 0 0 4.5 4.5L10 8l3 2-1.5 3C6 13 0 7 0 1.5z" fill="#f5cf0c"/></svg><span>(08) 5550 1427</span></p>
    <p class="contact-line"><svg width="14" height="11" viewBox="0 0 14 11"><rect width="14" height="11" rx="1" fill="#f5cf0c"/><path d="M0 1l7 5 7-5" stroke="#2a2a2a" fill="none"/></svg><span>info@veltrano.com</span></p>
    <h4 style="margin-top:26px">Location</h4>
    <div class="map" role="img" aria-label="Street map with office location pin"></div>
  </div>
  <div class="foot-col abs" style="left:880px;top:40px;width:240px">
    <h4>Association</h4>
    <div style="display:flex;gap:8px"><div class="badge-block" style="width:100px;height:70px"></div><div class="badge-block" style="width:100px;height:70px"></div></div>
    <div style="display:flex;gap:8px;margin-top:10px"><div class="badge-block" style="width:50px;height:90px;background:#c8262c"></div><div class="badge-block" style="width:50px;height:90px;background:#3a3a3a;border:1px solid #888"></div></div>
    <h4 style="margin-top:34px">Social Media</h4>
    <div class="social"><span></span><span></span><span></span><span></span><span></span></div>
  </div>
</footer>

<div class="copyright" style="position:relative;width:1200px">
  <p class="note abs">Copyright © 2016 VELTRANO | All Rights Reserved.</p>
  <div class="foot-brand abs"><span class="brand-dot" style="width:22px;height:22px"></span>Veltrano</div>
</div>

</body>
</html>
```